marlowe charters

We provide boar charter for :Fishing/whale watching and diving in Sydney Harbour providing for 12 passengersI have yet to have web page made but want to make logo first then do web page later. So I want to be able to edit and add this site to card later

Contact Information for Business Card

Captain Glen (Skip) Wigellphone no 0457710098email awigell4@gmail.comCompany name Brightwater Voyages Pty Ltd in association with open reef cruises

Font styles to use
Serif

Requirements
Nice to have
• perhaps a photo of boat and some stick diagrams of fishing.whales and diviving

```html
<!DOCTYPE html>
<html lang="en">
<head>
<meta charset="utf-8">
<title>Brightwater Voyages – Business Card</title>
<link rel="stylesheet" href="https://fonts.googleapis.com/css2?family=Marcellus&family=Noto+Serif:wght@700&display=swap">
<style>
  :root {
    --ink: #243f93;
    --card: #ffffff;
    --backdrop: #ece6dc;
    --shadow: rgba(60, 45, 25, 0.35);
  }
  * { box-sizing: border-box; margin: 0; padding: 0; }
  html, body { width: 1189px; height: 1200px; overflow: hidden; }
  body { background: var(--backdrop); position: relative; color: var(--ink); }

  .card {
    position: absolute;
    left: 171px;
    width: 855px;
    height: 487px;
    background: var(--card);
    border-radius: 20px;
    box-shadow: 10px 10px 14px var(--shadow);
  }
  .card--front { top: 67px; }
  .card--back  { top: 627px; }

  .brand {
    position: absolute;
    display: flex;
    flex-direction: column;
    align-items: center;
    font-family: "Marcellus", serif;
    color: var(--ink);
  }
  .brand__mark {
    width: 188px; height: 188px;
    border-radius: 50%;
    border: 9px solid var(--ink);
  }
  .brand__name {
    margin-top: 26px;
    font-size: 30px;
    line-height: 1;
    letter-spacing: 0.5px;
    white-space: nowrap;
  }
  .brand__suffix {
    margin-top: 8px;
    display: flex;
    align-items: center;
    gap: 12px;
    font-size: 20px;
    line-height: 1;
    white-space: nowrap;
  }
  .brand__suffix::before,
  .brand__suffix::after {
    content: "";
    width: 104px;
    height: 2px;
    background: var(--ink);
    margin-top: 10px;
  }
  .card--front .brand { left: 0; right: 0; top: 115px; }
  .card--back .brand { left: 12px; width: 400px; top: 120px; }

  .divider {
    position: absolute;
    left: 427px; top: 92px;
    width: 1.5px; height: 302px;
    background: var(--ink);
  }

  .details {
    position: absolute;
    left: 469px; top: 108px;
    font-family: "Noto Serif", serif;
    font-weight: 700;
    color: var(--ink);
  }
  .details__company { font-size: 24px; line-height: 1.1; white-space: nowrap; }
  .details__partner { font-size: 14.5px; letter-spacing: 1.4px; line-height: 1.2; white-space: nowrap; }
  .details__person { margin-top: 52px; font-size: 44px; line-height: 1; }
  .contact { list-style: none; margin-top: 38px; }
  .contact__item {
    display: flex; align-items: center; gap: 16px;
    font-size: 24px; line-height: 1; height: 28px;
    margin-bottom: 11px;
    white-space: nowrap;
  }
  .contact__icon { width: 27px; height: 27px; flex: none; }
</style>
</head>
<body>
  <section class="card card--front">
    <div class="brand">
      <div class="brand__mark"></div>
      <div class="brand__name">BRIGHTWATER VOYAGES</div>
      <div class="brand__suffix">PTY LTD</div>
    </div>
  </section>

  <section class="card card--back">
    <div class="brand">
      <div class="brand__mark"></div>
      <div class="brand__name">BRIGHTWATER VOYAGES</div>
      <div class="brand__suffix">PTY LTD</div>
    </div>

    <div class="divider"></div>

    <div class="details">
      <p class="details__company">Brightwater Voyages Pty Ltd</p>
      <p class="details__partner">in association with open reef cruises</p>
      <p class="details__person">Ferrant</p>
      <ul class="contact">
        <li class="contact__item">
          <svg class="contact__icon" viewBox="0 0 27 27" aria-hidden="true">
            <rect width="27" height="27" rx="3" fill="var(--ink)"/>
            <path d="M6 11 Q13.5 5 21 11 L19 13 L16.5 11.5 L16.5 10 Q13.5 9 10.5 10 L10.5 11.5 L8 13 Z" fill="#fff"/>
            <path d="M9 14 L18 14 L20 20 L7 20 Z" fill="#fff"/>
            <circle cx="13.5" cy="16.8" r="1.8" fill="var(--ink)"/>
          </svg>
          0462385147
        </li>
        <li class="contact__item">
          <svg class="contact__icon" viewBox="0 0 27 27" aria-hidden="true">
            <rect width="27" height="27" rx="3" fill="var(--ink)"/>
            <rect x="5" y="8" width="17" height="12" fill="none" stroke="#fff" stroke-width="1.6"/>
            <path d="M5 8 L13.5 15 L22 8 M5 20 L11 14 M22 20 L16 14" fill="none" stroke="#fff" stroke-width="1.4"/>
          </svg>
          gferrant7@tidemail.net
        </li>
      </ul>
    </div>
  </section>
</body>
</html>
```